(4) Bowling League Designs 1920x1080

Will be used on our website and in some digital signage.

We are starting (4) leagues this summer and need a basic graphic as an attention grab which will then lead the customer to full information / sign ups. The information I would need on each one is as follows:

1. Monday Night FREE ball league - Begins May 3rd

2. Tuesday Trios - KFDL Sanctioned - Begins May 11th
$9,000 prize fund

3. Wednesday Cosmic League - 9 pin no tap fun league - May 12th start

4. Thursday Night FREE ball league - Begins May 13th

I will attach some random examples of previous ones to give you an idea.

```html
<!DOCTYPE html>
<html lang="en">
<head>
<meta charset="utf-8">
<title>Tuesday Trios League Banner</title>
<link href="https://fonts.googleapis.com/css2?family=Barlow+Condensed:ital,wght@1,500;1,800&family=Montserrat:ital,wght@0,500;1,800&display=swap" rel="stylesheet">
<style>
  :root {
    --page: #e6e6e6;
    --black: #060606;
    --panel: #1c1c1c;
    --white: #ffffff;
    --gold: #f2b705;
    --silver-hi: #ffffff;
    --silver-mid: #b9bcc2;
    --silver-lo: #6c7078;
    --lane-blue: #3a4fd6;
    --lane-violet: #8a5ce0;
    --lane-deep: #1a2070;
    --shirt: #d8262a;
    --denim: #2f3f5c;
  }
  * { margin: 0; padding: 0; box-sizing: border-box; }
  html, body { width: 1200px; height: 796px; overflow: hidden; background: var(--page); }
  .banner {
    position: absolute; left: 72px; top: 75px;
    width: 1056px; height: 594px;
    background: var(--black); overflow: hidden;
  }
  .banner-art { position: absolute; inset: 0; }
  .headline, .sanction, .start-date, .prize-label, .prize-amount {
    position: absolute; left: 28px; white-space: nowrap;
  }
  .silver {
    background: linear-gradient(180deg, var(--silver-hi) 10%, var(--silver-mid) 48%, var(--silver-lo) 55%, var(--silver-hi) 95%);
    -webkit-background-clip: text; background-clip: text; color: transparent;
    padding-right: 24px;
  }
  .headline {
    top: 52px;
    font: italic 800 120px/1 "Barlow Condensed", sans-serif;
    letter-spacing: -2px;
    -webkit-text-stroke: 1px rgba(242,183,5,0.55);
  }
  .sanction {
    top: 181px; left: 32px;
    font: italic 800 54px/1 "Montserrat", sans-serif;
    color: var(--white);
  }
  .start-date {
    top: 275px;
    font: italic 500 86px/1 "Barlow Condensed", sans-serif;
    letter-spacing: -1px;
    color: var(--white);
  }
  .start-date .date { color: var(--gold); font-weight: 800; }
  .prize-label {
    top: 404px; left: 32px;
    display: flex; align-items: center; gap: 8px;
    font: 500 20px/1 "Montserrat", sans-serif;
    letter-spacing: 3px; color: var(--white);
  }
  .prize-label .rule { width: 125px; height: 2px; background: var(--gold); }
  .prize-amount {
    top: 419px;
    font: italic 800 120px/1 "Barlow Condensed", sans-serif;
    letter-spacing: -3px;
  }
</style>
</head>
<body>
  <section class="banner">
    <svg class="banner-art" viewBox="0 0 1056 594" width="1056" height="594">
      <defs>
        <linearGradient id="lanes" x1="0" y1="0" x2="1" y2="1">
          <stop offset="0" stop-color="var(--lane-violet)"/>
          <stop offset="0.45" stop-color="var(--lane-blue)"/>
          <stop offset="1" stop-color="var(--lane-deep)"/>
        </linearGradient>
        <linearGradient id="bowler" x1="0" y1="0" x2="0" y2="1">
          <stop offset="0" stop-color="var(--shirt)"/>
          <stop offset="0.38" stop-color="var(--shirt)"/>
          <stop offset="0.52" stop-color="var(--denim)"/>
          <stop offset="1" stop-color="var(--denim)"/>
        </linearGradient>
      </defs>
      <polygon class="dark-panel" points="428,0 733,0 817,594 511,594" fill="var(--panel)"/>
      <polygon class="lanes-photo" role="img" aria-label="Photo of glowing bowling lanes with pins under coloured lights"
               points="733,0 1056,0 1056,594 817,594" fill="url(#lanes)"/>
      <rect class="bowler-photo" role="img" aria-label="Photo of a bowler in a red polo and jeans releasing a red bowling ball"
            x="668" y="30" width="300" height="564" rx="40" fill="url(#bowler)" opacity="0.9"/>
      <circle class="ring" cx="615" cy="425" r="62" fill="none" stroke="var(--white)" stroke-width="1.5" stroke-dasharray="2 5"/>
      <line class="accent-line" x1="713" y1="300" x2="747" y2="592" stroke="var(--white)" stroke-width="2"/>
      <line class="accent-line" x1="778" y1="0" x2="797" y2="120" stroke="var(--white)" stroke-width="2"/>
      <g class="dot-row" fill="var(--white)">
        <circle cx="34" cy="568" r="2"/><circle cx="49" cy="568" r="2"/><circle cx="64" cy="568" r="2"/>
        <circle cx="79" cy="568" r="2"/><circle cx="94" cy="568" r="2"/><circle cx="109" cy="568" r="2"/>
        <circle cx="124" cy="568" r="2"/><circle cx="139" cy="568" r="2"/><circle cx="154" cy="568" r="2"/>
        <circle cx="169" cy="568" r="2"/><circle cx="184" cy="568" r="2"/><circle cx="199" cy="568" r="2"/>
        <circle cx="214" cy="568" r="2"/><circle cx="229" cy="568" r="2"/><circle cx="244" cy="568" r="2"/>
        <circle cx="259" cy="568" r="2"/><circle cx="274" cy="568" r="2"/><circle cx="289" cy="568" r="2"/>
        <circle cx="304" cy="568" r="2"/><circle cx="319" cy="568" r="2"/><circle cx="334" cy="568" r="2"/>
      </g>
    </svg>

    <h1 class="headline silver">TUESDAY TRIOS</h1>
    <p class="sanction">KFDL SANCTIONED</p>
    <p class="start-date">BEGINS <span class="date">MAY 11</span></p>
    <p class="prize-label">PRIZE FUND <span class="rule"></span></p>
    <p class="prize-amount silver">$9,000</p>
  </section>
</body>
</html>
```